Locksmith business card design

i need a business card design for a new locksmith/auto Locksmith company we cater for residental/commercial/industrial/vehicles locksmithing we provide a 24/7 emergency service we are fully insured and certified i like the idea of black with white writing i would like the final design to communicate we are very affordable compared to our competitors

Target Market(s)

everyone

Industry/Entity Type

Business

Contact Information for Business Card

Bramwell's 24h Locksmiths, Owen Bramwell, 27 fenwick lane ashcombe vale so482kt, bramwells_locksmiths@quillmail.com,07841296035,www.bramwellslocksmith.com

Requirements
Must have
• some sort of logo/picture

```html
<!DOCTYPE html>
<html lang="en">
<head>
<meta charset="utf-8">
<title>Bramwell's 24h Locksmiths – Business Card</title>
<link rel="stylesheet" href="https://fonts.googleapis.com/css2?family=Marcellus&family=PT+Sans:wght@400&display=swap">
<style>
  :root {
    --backdrop: #6d6e71;
    --ink: #000000;
    --paper: #ffffff;
    --placeholder-light: #f2f2f2;
    --placeholder-grey: #d8d7d8;
    --title-font: "Marcellus", "Optima", serif;
    --body-font: "PT Sans", "Myriad Pro", sans-serif;
  }
  * { margin: 0; padding: 0; box-sizing: border-box; }
  html, body {
    width: 1200px;
    height: 1000px;
    overflow: hidden;
    background: var(--backdrop);
  }
  .canvas {
    position: relative;
    width: 1200px;
    height: 1000px;
  }
  .card {
    position: absolute;
    width: 637px;
    height: 420px;
    overflow: hidden;
  }

  /* Front side */
  .card-front {
    left: 52px;
    top: 42px;
    background: var(--ink);
    color: var(--paper);
  }
  .card-front .title {
    position: absolute;
    left: 0;
    width: 100%;
    top: 182px;
    text-align: center;
    font-family: var(--title-font);
    font-weight: 400;
    font-size: 54px;
    letter-spacing: 1px;
    line-height: 1;
    white-space: nowrap;
  }
  .card-front .website {
    position: absolute;
    left: 0;
    width: 100%;
    top: 241px;
    text-align: center;
    font-family: var(--body-font);
    font-size: 17px;
    letter-spacing: 0.5px;
    line-height: 1;
  }
  .card-front .artwork-area {
    position: absolute;
    left: 0;
    bottom: 0;
    width: 637px;
    height: 130px;
    background: linear-gradient(180deg, var(--placeholder-light), var(--paper));
  }

  /* Back side */
  .card-back {
    left: 475px;
    top: 536px;
    background: var(--paper);
    color: var(--ink);
  }
  .card-back .title {
    position: absolute;
    left: 41px;
    top: 178px;
    font-family: var(--title-font);
    font-weight: 400;
    font-size: 37px;
    letter-spacing: 0.5px;
    line-height: 1;
    white-space: nowrap;
  }
  .card-back .tagline {
    position: absolute;
    left: 41px;
    top: 216px;
    font-family: var(--body-font);
    font-size: 21px;
    letter-spacing: 1px;
    line-height: 1;
  }
  .card-back .rule {
    position: absolute;
    left: 0;
    top: 250px;
    width: 394px;
    height: 3px;
    background: var(--ink);
  }
  .contact-list {
    position: absolute;
    left: 41px;
    top: 271px;
    list-style: none;
    font-family: var(--body-font);
    line-height: 1;
    white-space: nowrap;
  }
  .contact-list li { margin-bottom: 12px; font-size: 15px; }
  .contact-list li.phone { font-size: 17px; }
  .card-back .artwork-area {
    position: absolute;
    left: 453px;
    top: 170px;
    width: 103px;
    height: 175px;
    background: var(--placeholder-grey);
  }
  .card-back .footer-band {
    position: absolute;
    left: 0;
    bottom: 0;
    width: 100%;
    height: 53px;
    background: var(--ink);
    color: var(--paper);
    font-family: var(--body-font);
    font-size: 15px;
    line-height: 53px;
    padding-left: 44px;
    white-space: nowrap;
  }
</style>
</head>
<body>
<main class="canvas">
  <section class="card card-front">
    <h1 class="title">AUTO LOCKSMITH</h1>
    <p class="website">www.bramwellslocksmith.com</p>
    <div class="artwork-area" role="img" aria-label="Large white key illustration along the bottom edge"></div>
  </section>

  <section class="card card-back">
    <h2 class="title">AUTO LOCKSMITH</h2>
    <p class="tagline">24/7 emergency service</p>
    <div class="rule"></div>
    <ul class="contact-list">
      <li class="email">[ Email: bramwells_locksmiths@quillmail.com ]</li>
      <li class="phone">[ Phone: 07841296035 ]</li>
      <li class="web">[ Web: www.bramwellslocksmith.com ]</li>
    </ul>
    <div class="artwork-area" role="img" aria-label="Light grey keyhole illustration"></div>
    <div class="footer-band">Bramwell's 24h Locksmiths, Owen Bramwell, 27 fenwick lane ashcombe vale so482kt</div>
  </section>
</main>
</body>
</html>
```